Facebook & Instagram Ad Design for Chiropractor

I'd like a series of ads developed for our chiropractic office to use on Facebook and Instagram. I've attached the versions we're using today. They need to be updated. The offer content would be generally the same. There are two types of ads we're seeking. One for basic chiropractic services and the other for chiropractic decompression services.

Current ads can be seen in attached and here:
https://lnk.example/8TrQ2zXvPoLkm3A

Learn more about the company at www.bellwingchiropractic.example

Target Market(s)

Potential patients seeking chiropractic care or who are unaware that chiropractic could help them (suffer from back pain, etc.) in the greater Green Bay, WI area.

Industry/Entity Type

Chiropractic

Font styles to use
Sans Serif

Colors
0592cd
3277b5

Requirements
Must have
• Compelling visuals
Comply with text requirements for FB & Insta ads
Should not have
• Clinical images that depict traditional medical care

```html
<!DOCTYPE html>
<html lang="en">
<head>
<meta charset="utf-8">
<title>Bellwing Chiropractic – Social Ads</title>
<link rel="stylesheet" href="https://fonts.googleapis.com/css2?family=Montserrat:wght@400&family=Open+Sans:wght@400;700;800&family=Roboto+Condensed:wght@700&display=swap">
<style>
  :root {
    --navy: #1c2940;
    --maroon: #6b1a2e;
    --teal: #2f86a6;
    --white: #ffffff;
    --page: #f2efe9;
    --sky-top: #e6f2f6;
    --sky-bottom: #f6f8f7;
    --caption: #2a2a2a;
    --frame: #c9ccd0;
  }
  html, body {
    margin: 0;
    width: 1200px;
    height: 679px;
    overflow: hidden;
    background: var(--page);
  }
  .board { position: relative; width: 1200px; height: 679px; }
  .ad-caption {
    position: absolute;
    top: 70px;
    width: 443px;
    margin: 0;
    text-align: center;
    font: 400 20px "Montserrat", sans-serif;
    color: var(--caption);
    letter-spacing: 0.2px;
  }
  .ad {
    position: absolute;
    top: 120px;
    width: 443px;
    height: 443px;
    box-shadow: 6px 8px 14px rgba(0,0,0,0.25);
  }
  .ad svg { display: block; width: 443px; height: 443px; }
  .ad--basic, .caption--basic { left: 82px; }
  .ad--decompression, .caption--decompression { left: 664px; }
  .brand { font-family: "Roboto Condensed", sans-serif; font-weight: 700; fill: var(--navy); }
  .offer { font-family: "Open Sans", sans-serif; font-weight: 800; fill: var(--white); }
  .headline { font-family: "Open Sans", sans-serif; font-weight: 800; }
  .url { font-family: "Open Sans", sans-serif; font-size: 10.5px; fill: var(--white); }
</style>
</head>
<body>
<main class="board">
  <h2 class="ad-caption caption--basic">Basic Chiropractic Services Ad</h2>
  <h2 class="ad-caption caption--decompression">Chiropractic Decompression Services Ad</h2>

  <section class="ad ad--basic" aria-label="Basic chiropractic services ad">
    <svg viewBox="0 0 443 443" xmlns="http://www.w3.org/2000/svg">
      <defs>
        <linearGradient id="sky" x1="0" y1="0" x2="0" y2="1">
          <stop offset="0" stop-color="var(--sky-top)"/>
          <stop offset="1" stop-color="var(--sky-bottom)"/>
        </linearGradient>
        <linearGradient id="beach" x1="0" y1="0" x2="0" y2="1">
          <stop offset="0" stop-color="#bcdbe2"/>
          <stop offset="1" stop-color="#e8e2d6"/>
        </linearGradient>
        <linearGradient id="adjust" x1="0" y1="0" x2="1" y2="1">
          <stop offset="0" stop-color="#eef1f3"/>
          <stop offset="0.5" stop-color="#7c9fb3"/>
          <stop offset="1" stop-color="#d7cabe"/>
        </linearGradient>
        <linearGradient id="badge" x1="0" y1="0" x2="0" y2="1">
          <stop offset="0" stop-color="#8a2f45"/>
          <stop offset="0.5" stop-color="var(--maroon)"/>
        </linearGradient>
      </defs>
      <rect class="sky" width="443" height="443" fill="url(#sky)"/>
      <path class="corner-band" d="M287 81 C310 30 360 0 390 0 L443 0 L443 81 Z" fill="var(--navy)"/>
      <rect class="beach-photo" role="img" aria-label="Family running along a sunny beach" x="0" y="264" width="230" height="179" fill="url(#beach)"/>
      <path class="photo-frame" d="M152 330 C150 260 210 100 260 85 L443 81 L443 365 L190 365 C165 365 152 352 152 330 Z" fill="var(--frame)"/>
      <path class="adjust-photo" role="img" aria-label="Chiropractor's hands adjusting a patient's lower back" d="M157 328 C156 262 214 106 262 90 L443 86 L443 360 L190 360 C170 360 157 348 157 328 Z" fill="url(#adjust)"/>
      <path class="bottom-band" d="M195 363 L443 363 L443 443 L245 443 C215 443 195 418 195 395 Z" fill="var(--navy)"/>
      <text class="url" x="241" y="406">www.<tspan font-weight="700">greenbay-spinecare</tspan>.example</text>
      <path class="badge-back" d="M70 125 C110 110 160 130 170 170 C182 215 150 245 100 243 C60 241 35 220 32 185 C30 155 45 133 70 125 Z" fill="var(--teal)"/>
      <path class="badge" d="M80 122 C130 112 160 137 160 177 C160 222 135 245 95 244 C55 243 25 216 26 186 C27 151 45 129 80 122 Z" fill="url(#badge)" stroke="var(--frame)" stroke-width="2"/>
      <text class="offer" font-size="17" text-anchor="middle" x="95" y="180">New Patient</text>
      <text class="offer" font-size="17" text-anchor="middle" x="95" y="203">Offer $25!</text>
      <text class="brand" font-size="38" x="20" y="60" textLength="257" lengthAdjust="spacingAndGlyphs">Bellwing Chiropractic</text>
      <line class="brand-rule" x1="19" y1="67" x2="278" y2="67" stroke="var(--maroon)" stroke-width="1.5"/>
    </svg>
  </section>

  <section class="ad ad--decompression" aria-label="Chiropractic decompression services ad">
    <svg viewBox="0 0 443 443" xmlns="http://www.w3.org/2000/svg">
      <defs>
        <linearGradient id="table" x1="0" y1="0" x2="1" y2="1">
          <stop offset="0" stop-color="#eef0f1"/>
          <stop offset="0.5" stop-color="#c8ccd0"/>
          <stop offset="1" stop-color="#3a4a66"/>
        </linearGradient>
      </defs>
      <rect width="443" height="443" fill="var(--white)"/>
      <text class="brand" font-size="38" text-anchor="middle" x="227" y="62" textLength="244" lengthAdjust="spacingAndGlyphs">Bellwing Chiropractic</text>
      <line class="brand-rule" x1="104" y1="68" x2="350" y2="68" stroke="var(--maroon)" stroke-width="1.5"/>
      <text class="headline" font-size="20" fill="var(--maroon)" text-anchor="middle" x="222" y="103">Spinal Decompression Therapy</text>
      <text class="headline" font-size="20" fill="var(--navy)" text-anchor="middle" x="222" y="131">in Green Bay</text>
      <path class="wave" d="M0 233 C25 270 50 330 110 335 C200 345 250 290 300 250 C340 218 380 215 443 225 L443 443 L0 443 Z" fill="var(--navy)"/>
      <path class="photo-outline" d="M150 152 C220 140 300 155 350 200 C385 240 385 340 330 392 C290 420 230 375 170 370 C120 365 75 350 65 300 C55 240 90 165 150 152 Z" fill="none" stroke="var(--maroon)" stroke-width="1"/>
      <path class="decompression-photo" role="img" aria-label="Patient lying on a spinal decompression table" d="M150 160 C220 148 295 162 340 205 C372 242 372 335 322 382 C285 408 230 368 172 362 C126 357 84 343 75 298 C66 243 98 172 150 160 Z" fill="url(#table)"/>
      <path class="photo-outline-light" d="M150 155 C222 143 300 158 347 203 C382 242 380 340 326 388" fill="none" stroke="var(--white)" stroke-width="1"/>
      <path class="offer-band" d="M5 443 L5 395 C10 355 50 333 100 333 C160 333 206 370 206 410 L206 443 Z" fill="var(--maroon)"/>
      <text class="offer" font-size="21" text-anchor="middle" x="105" y="393">New Patient</text>
      <text class="offer" font-size="21" text-anchor="middle" x="105" y="420">Special $25!</text>
      <text class="url" x="248" y="417">www.<tspan font-weight="700">greenbay-spinecare</tspan>.example</text>
    </svg>
  </section>
</main>
</body>
</html>
```